VorluĀ®? Cartridge Box

Vorlu is a new, patent pending nebulizer-like technology. It comes with disposable, 12 ml cartridges. We are wanting an design an outer, retail box for the cartridge. The box is white, its size is a 35mm x 35mm x 90mm, the typical size for a 30 ml boston Round tincture bottle.

```html
<!DOCTYPE html>
<html lang="en">
<head>
<meta charset="utf-8">
<title>Vorlu® Cartridge Box – Dieline</title>
<link rel="stylesheet" href="https://fonts.googleapis.com/css2?family=Open+Sans:wght@400;700&family=Bitter:ital,wght@1,300&family=Cormorant+Garamond:ital,wght@1,500&display=swap">
<style>
  :root {
    --page: #f2f2f2;
    --board: #2f2f2f;
    --board-light: #353433;
    --board-edge: #262626;
    --cyan: #2fcde4;
    --ink-light: #f1f1f1;
    --ink-soft: #d6d6d6;
    --ink-dark: #1d2a33;
  }
  * { margin: 0; padding: 0; box-sizing: border-box; }
  html, body { width: 1200px; height: 853px; overflow: hidden; background: var(--page); }
  .canvas { position: relative; width: 1200px; height: 853px; }
  .dieline { position: absolute; inset: 0; }
  .label { position: absolute; transform: translate(-50%, -50%); white-space: nowrap; text-align: center; }
  .brand { font-family: "Open Sans", sans-serif; font-weight: 700; font-size: 25px; color: var(--ink-light); display: flex; align-items: center; gap: 6px; letter-spacing: 0.5px; }
  .brand-dot { width: 12px; height: 12px; border-radius: 50%; background: var(--cyan); }
  .brand sup { font-size: 9px; font-weight: 700; vertical-align: 14px; }
  .product { display: flex; align-items: center; gap: 4px; font-family: "Bitter", serif; font-style: italic; font-weight: 300; font-size: 16px; color: var(--ink-light); }
  .product-dot { width: 28px; height: 28px; border-radius: 50%; background: var(--cyan); }
  .blend { font-family: "Bitter", serif; font-style: italic; font-weight: 300; font-size: 11.5px; line-height: 14px; color: var(--ink-light); }
  .patent { font-family: "Open Sans", sans-serif; font-size: 7px; line-height: 9px; color: var(--ink-soft); }
  .band-text { font-family: "Cormorant Garamond", serif; font-style: italic; font-weight: 500; font-size: 11px; color: var(--ink-dark); }
  .variant { position: absolute; left: 571px; top: 454px; font-family: "Open Sans", sans-serif; font-size: 7.5px; color: var(--ink-light); display: flex; align-items: center; gap: 2px; }
  .variant-tag { background: var(--cyan); color: var(--ink-dark); padding: 0 2px; }
  .ingredients { position: absolute; left: 562px; top: 477px; font-family: "Open Sans", sans-serif; font-size: 7.5px; color: var(--ink-soft); }
  .ingredients h2 { font-size: 7.5px; font-weight: 400; margin-bottom: 9px; }
  .ingredients ul { list-style: none; }
  .ingredients li { line-height: 10.5px; }
  .ingredients li::before { content: "-"; display: inline-block; width: 10px; }
</style>
</head>
<body>
<div class="canvas">
  <svg class="dieline" viewBox="0 0 1200 853" width="1200" height="853" aria-hidden="true">
    <!-- top flaps -->
    <path d="M328 244 L331 200 Q333 185 350 185 L425 184 L429 244 L436 257 L317 257 L317 250 Z" fill="var(--board)"/>
    <path d="M434 257 L434 133 Q434 115 455 115 L530 114 Q551 114 551 133 L552 257 Z" fill="var(--board)"/>
    <line x1="435" y1="139" x2="551" y2="138" stroke="var(--board-edge)" stroke-width="1"/>
    <path d="M553 257 L557 243 L561 196 Q562 184 572 184 L648 184 Q651 184 652 190 L658 240 L667 246 L669 257 Z" fill="var(--board)"/>
    <!-- body panels -->
    <rect x="317" y="257" width="119" height="357" fill="var(--board)"/>
    <rect x="436" y="257" width="117" height="357" fill="var(--board-light)"/>
    <rect x="553" y="257" width="116" height="355" fill="var(--board-light)"/>
    <rect x="669" y="256" width="118" height="356" fill="var(--board)"/>
    <path d="M787 256 L822 266 L828 596 L787 611 Z" fill="var(--board)"/>
    <!-- bottom flaps -->
    <path d="M321 614 L441 614 L441 628 L431 638 L426 676 Q424 687 413 687 L334 688 L331 628 Z" fill="var(--board)"/>
    <path d="M553 612 L669 612 L661 627 L661 684 L578 685 Q566 685 565 675 L561 634 L554 627 Z" fill="var(--board)"/>
    <path d="M670 612 L789 612 L790 739 Q790 757 771 757 L693 758 Q675 758 675 741 Z" fill="var(--board)"/>
    <line x1="675" y1="741" x2="790" y2="740" stroke="var(--board-edge)" stroke-width="1"/>
    <!-- fold lines -->
    <g stroke="var(--board-edge)" stroke-width="0.8">
      <line x1="436" y1="257" x2="440" y2="614"/>
      <line x1="553" y1="257" x2="553" y2="612"/>
      <line x1="669" y1="257" x2="669" y2="612"/>
      <line x1="787" y1="256" x2="787" y2="612"/>
    </g>
    <!-- cartridge band -->
    <rect x="440" y="590" width="348" height="14" fill="var(--cyan)"/>
  </svg>

  <!-- front panel -->
  <div class="label brand" style="left:494px; top:333px;"><span class="brand-dot"></span>Vorlu<sup>®</sup></div>
  <div class="label product" style="left:494px; top:409px;"><span class="product-dot"></span>Vorasol</div>
  <div class="label blend" style="left:496px; top:495px;">Anti<br>Nausea Blend</div>
  <div class="label patent" style="left:497px; top:568px;">Patent Pending<br>Nebulizer</div>
  <div class="label band-text" style="left:499px; top:597px;">12 ml cartridges</div>

  <!-- ingredients panel -->
  <div class="label blend" style="left:608px; top:409px;">Anti<br>Nausea Blend</div>
  <div class="variant">VORASOL <span class="variant-tag">MENTHOL</span></div>
  <div class="ingredients">
    <h2>Ingredients:</h2>
    <ul>
      <li>Purified Water</li>
      <li>Vegetable Glycerin</li>
      <li>Cannabidieth-21</li>
      <li>Sodium Chloride</li>
      <li>Potassium Sorbate</li>
      <li>Menthol</li>
      <li>Sodium Benzoate.</li>
    </ul>
  </div>
  <div class="label band-text" style="left:611px; top:596px;">12 ml cartridges</div>

  <!-- back panel -->
  <div class="label brand" style="left:727px; top:331px;"><span class="brand-dot"></span>Vorlu<sup>®</sup></div>
  <div class="label product" style="left:728px; top:402px;"><span class="product-dot"></span>Vorasol</div>
  <div class="label blend" style="left:729px; top:489px;">Anti<br>Nausea Blend</div>
  <div class="label patent" style="left:730px; top:564px;">Patent Pending<br>Nebulizer</div>
  <div class="label band-text" style="left:731px; top:595px;">12 ml cartridges</div>
</div>
</body>
</html>
```